New Business Card Design Project

Would like you to take my logo and create a business card much like the Bramblecove leasing.
I can get you the fonts used for the back of the card.
I want the same speckled blue with my logo on it.

Feel free to improve upon the balloon part of the logo if you can.
I put one I was doing with a new balloon and a more "string-like" "I".

```html
<!DOCTYPE html>
<html lang="en">
<head>
<meta charset="utf-8">
<title>Larkspur Real Estate – Business Card</title>
<link rel="stylesheet" href="https://fonts.googleapis.com/css2?family=Cinzel:wght@400&family=EB+Garamond:wght@400&display=swap">
<style>
  :root {
    --backdrop: #e6e6e6;
    --card-white: #ffffff;
    --navy: #0a0a3e;
    --leaf: #76a83a;
    --ink-grey: #4a4a5a;
    --white: #ffffff;
  }
  * { box-sizing: border-box; margin: 0; padding: 0; }
  html, body {
    width: 1200px;
    height: 675px;
    overflow: hidden;
    background: var(--backdrop);
  }
  .canvas {
    position: relative;
    width: 1200px;
    height: 675px;
    display: flex;
    align-items: center;
    justify-content: center;
    gap: 60px;
  }
  .card {
    position: relative;
    width: 500px;
    height: 286px;
    box-shadow: 0 2px 8px rgba(0,0,0,0.12);
  }
  .card--front { background: var(--card-white); }
  .card--back { background: var(--navy); }

  .wordmark {
    display: flex;
    align-items: center;
    gap: 12px;
    font-family: "Cinzel", serif;
    font-weight: 400;
    letter-spacing: 0.06em;
  }
  .wordmark__dot {
    width: 22px;
    height: 22px;
    border-radius: 50%;
    background: var(--leaf);
    flex: none;
  }
  .wordmark__name {
    font-size: 24px;
    line-height: 1.1;
  }
  .wordmark__line { display: block; white-space: nowrap; }

  .card--front .wordmark {
    position: absolute;
    left: 34px;
    top: 112px;
    width: 230px;
  }
  .card--front .wordmark__name { color: var(--navy); }

  .identity {
    position: absolute;
    left: 300px;
    top: 34px;
    color: var(--navy);
  }
  .identity__name {
    font-family: "Cinzel", serif;
    font-size: 15px;
    letter-spacing: 0.04em;
  }
  .identity__title {
    font-family: "EB Garamond", serif;
    font-size: 12px;
    color: var(--ink-grey);
    margin-top: 2px;
  }

  .contact {
    position: absolute;
    left: 300px;
    top: 104px;
    list-style: none;
    font-family: "EB Garamond", serif;
    font-size: 12px;
    color: var(--navy);
  }
  .contact__item {
    display: flex;
    align-items: flex-start;
    gap: 9px;
    margin-bottom: 7px;
    line-height: 1.35;
  }
  .contact__icon {
    width: 11px;
    height: 11px;
    flex: none;
    margin-top: 2px;
    fill: var(--leaf);
  }
  .contact__icon-cut {
    fill: none;
    stroke: var(--white);
    stroke-width: 2;
  }

  .card--back .wordmark {
    position: absolute;
    left: 50%;
    top: 100px;
    transform: translateX(-50%);
  }
  .card--back .wordmark__name { color: var(--white); text-align: center; }
  .back__url {
    position: absolute;
    left: 0;
    right: 0;
    top: 204px;
    text-align: center;
    font-family: "EB Garamond", serif;
    font-size: 12px;
    color: var(--white);
    letter-spacing: 0.02em;
  }
</style>
</head>
<body>
<main class="canvas">
  <section class="card card--front" aria-label="Card front">
    <div class="wordmark">
      <span class="wordmark__dot"></span>
      <span class="wordmark__name">
        <span class="wordmark__line">Larkspur</span>
        <span class="wordmark__line">Real Estate</span>
      </span>
    </div>

    <div class="identity">
      <p class="identity__name">WREN HALLOWAY</p>
      <p class="identity__title">Owner &amp; Founder</p>
    </div>

    <ul class="contact">
      <li class="contact__item">
        <svg class="contact__icon" viewBox="0 0 24 24" aria-hidden="true"><path d="M6.6 10.8a15.1 15.1 0 0 0 6.6 6.6l2.2-2.2a1 1 0 0 1 1-.25 11.4 11.4 0 0 0 3.6.57 1 1 0 0 1 1 1V20a1 1 0 0 1-1 1A17 17 0 0 1 3 4a1 1 0 0 1 1-1h3.5a1 1 0 0 1 1 1c0 1.25.2 2.45.57 3.57a1 1 0 0 1-.25 1z"/></svg>
        <span>(555) 014-2290</span>
      </li>
      <li class="contact__item">
        <svg class="contact__icon" viewBox="0 0 24 24" aria-hidden="true"><path d="M2 5h20v14H2z"/><path class="contact__icon-cut" d="M3 6l9 7 9-7"/></svg>
        <span>wrenhalloway@mail.com</span>
      </li>
      <li class="contact__item">
        <svg class="contact__icon" viewBox="0 0 24 24" aria-hidden="true"><path d="M12 2a10 10 0 1 0 0 20 10 10 0 0 0 0-20zm6.9 6h-2.9a15.6 15.6 0 0 0-1.4-3.6A8 8 0 0 1 18.9 8zM12 4a14 14 0 0 1 1.9 4h-3.8A14 14 0 0 1 12 4zM4.3 14a8 8 0 0 1 0-4h3.4a16 16 0 0 0 0 4zm.8 2h2.9a15.6 15.6 0 0 0 1.4 3.6A8 8 0 0 1 5.1 16zM8 8H5.1a8 8 0 0 1 4.3-3.6A15.6 15.6 0 0 0 8 8zm4 12a14 14 0 0 1-1.9-4h3.8A14 14 0 0 1 12 20zm2.3-6H9.7a14 14 0 0 1 0-4h4.6a14 14 0 0 1 0 4zm.3 5.6a15.6 15.6 0 0 0 1.4-3.6h2.9a8 8 0 0 1-4.3 3.6zm1.7-5.6a16 16 0 0 0 0-4h3.4a8 8 0 0 1 0 4z"/></svg>
        <span>www.larkspurrealty.com</span>
      </li>
      <li class="contact__item">
        <svg class="contact__icon" viewBox="0 0 24 24" aria-hidden="true"><path d="M12 2a7 7 0 0 0-7 7c0 5.2 7 13 7 13s7-7.8 7-13a7 7 0 0 0-7-7zm0 9.5A2.5 2.5 0 1 1 12 6.5a2.5 2.5 0 0 1 0 5z"/></svg>
        <span>42 Alder Row,<br>Millbrook, AL 35000</span>
      </li>
    </ul>
  </section>

  <section class="card card--back" aria-label="Card back">
    <div class="wordmark">
      <span class="wordmark__dot"></span>
      <span class="wordmark__name">
        <span class="wordmark__line">Larkspur</span>
        <span class="wordmark__line">Real Estate</span>
      </span>
    </div>
    <p class="back__url">www.larkspurrealty.com</p>
  </section>
</main>
</body>
</html>
```